We need a website so we can post future events of our company about business motivation. The site have to include a calendar on the "Home" page that when the user cliks on the day of the event , there should open a small page with the information of the event (location,time,subject of the event...) . We need also an "About Us" page with information about our company and what we do as well as "Contact" page with our email and phone number and access to our facebook page. We would like to have a private access for users ("Restricted access") but they have to put their e-mail and password to access the special page (log in). On the 'special page' we would like to have some videos and photos that we will post on that page regularly .
Here is a website that would be an exemple of how we would like to have ours
http://northvalecapitalhub.example
The needs to be responsed and with backoffice

Industry/Entity Type

Business

Number of Pages Required

3 page

Colors
9bcb3c
f37122

Requirements
Must have
• Must have a restricted access page so the user can place a user name and a secret password.

```html
<!DOCTYPE html>
<html lang="en">
<head>
<meta charset="utf-8">
<title>Brightpath7go – Business Events</title>
<link href="https://fonts.googleapis.com/css2?family=Open+Sans:wght@400;600;700&family=PT+Sans:wght@400;700&display=swap" rel="stylesheet">
<style>
:root{
  --orange:#f37122;
  --orange-dark:#d85e12;
  --green:#9bcb3c;
  --ink:#222222;
  --muted:#888888;
  --light:#f4f4f4;
  --footer:#161616;
  --footer-bar:#0d0d0d;
  --white:#ffffff;
}
*{margin:0;padding:0;box-sizing:border-box}
html,body{width:1200px;height:2525px;overflow:hidden}
body{font-family:"PT Sans",sans-serif;color:var(--ink);background:var(--white);position:relative}
h1,h2,h3,h4{font-family:"Open Sans",sans-serif}

/* Hero */
.hero{position:absolute;left:0;top:0;width:1200px;height:512px;
  background:radial-gradient(ellipse at 50% 30%,#6b86b3 0%,#3f5f93 45%,#1f3358 100%)}
.nav{position:absolute;left:112px;top:0;width:976px;height:88px;background:var(--white);
  display:flex;align-items:center;box-shadow:0 3px 8px rgba(0,0,0,.25)}
.brand{font-family:"Open Sans",sans-serif;font-weight:700;font-size:24px;color:var(--orange);margin-left:36px;flex:1}
.menu{display:flex;height:100%;list-style:none}
.menu li{display:flex;align-items:center;padding:0 19px;font-family:"Open Sans",sans-serif;font-size:12px;color:#333;text-transform:uppercase}
.menu li.active{background:var(--orange);color:var(--white);padding:0 24px;margin-right:4px}
.menu .search{padding:0 34px 0 20px}
.hero-title{position:absolute;top:300px;width:100%;text-align:center;color:var(--white);font-size:54px;font-weight:600;letter-spacing:1px}
.hero-text{position:absolute;top:375px;left:205px;width:790px;text-align:center;color:#e6ecf5;font-size:12px;line-height:25px}
.dots{position:absolute;top:474px;left:566px;display:flex;gap:8px}
.dots span{width:11px;height:11px;border-radius:50%;background:rgba(255,255,255,.5)}
.dots span.on{background:var(--green)}

/* Features */
.features{position:absolute;top:512px;left:0;width:1200px;height:368px;background:linear-gradient(135deg,#f7f7f7,#ececec 50%,#f7f7f7)}
.feature{position:absolute;top:56px;width:300px;text-align:center}
.feature .ring{width:116px;height:116px;margin:0 auto;border:3px solid var(--orange);border-radius:50%;background:var(--white);display:flex;align-items:center;justify-content:center}
.feature h3{margin-top:18px;font-size:17px;font-weight:600;color:#222}
.feature p{margin-top:8px;font-size:11px;line-height:27px;color:#666}

/* Calendar section */
.calendar-section{position:absolute;top:880px;left:0;width:1200px;height:553px;
  background:radial-gradient(ellipse at 60% 20%,#c06a2a 0%,#6a2f0e 45%,#1a0c05 100%)}
.section-title{text-align:center;font-size:29px;font-weight:700;color:var(--white)}
.calendar-section .section-title{position:absolute;top:76px;width:100%}
.event-box{position:absolute;top:148px;left:112px;width:976px;height:327px;border:2px solid var(--orange);border-radius:4px;background:var(--light);display:flex;overflow:hidden}
.month{width:285px;background:#fff;border-right:1px solid #ccc}
.month-head{height:55px;background:linear-gradient(#f4f4f4,#cfcfcf);display:flex;align-items:center;justify-content:space-between;padding:0 18px;font-family:Arial,sans-serif;font-weight:700;font-size:21px;color:#333}
.month-head .arr{font-size:13px;color:#444}
.month-head .arr.next{color:#999}
.days{width:100%;border-collapse:collapse;font-family:Arial,sans-serif;font-size:16px;text-align:center}
.days th{height:26px;font-size:14px;font-weight:400;color:#333;border:1px solid #ccc;background:#f2f2f2}
.days td{height:40px;border:1px solid #ccc;background:#f6f6f6;color:#222}
.days td.out{color:#aaa;background:#fafafa}
.days td.sat{background:#e4e4e4}
.days td.mark{background:#8a8a8a;color:#fff}
.days td.today{color:#2a7ab8}
.days td.sel{background:var(--orange);color:#fff}
.agenda{flex:1}
.agenda-head{height:55px;background:linear-gradient(var(--orange),var(--orange-dark));color:#fff;font-family:"Open Sans",sans-serif;font-weight:600;font-size:17px;padding:17px 42px}
.agenda-item{display:flex;margin:20px 0 0 36px}
.agenda-item + .agenda-item{margin-top:26px}
.agenda-item .thumb{width:130px;height:86px;border:3px solid #fff;box-shadow:0 6px 6px -3px rgba(0,0,0,.45);flex:none}
.agenda-item .body{margin-left:20px;width:490px}
.agenda-item h4{font-size:15px;font-weight:600;color:var(--orange);text-transform:uppercase}
.agenda-item p{margin-top:6px;font-size:11px;line-height:26px;color:#777}
.more{margin-top:4px;font-size:11px;color:var(--green);text-transform:uppercase;font-family:"Open Sans",sans-serif}

/* Latest events */
.latest{position:absolute;top:1433px;left:0;width:1200px;height:339px;background:#fff}
.latest .section-title{color:var(--ink);position:absolute;top:50px;width:100%}
.post{position:absolute;top:130px;display:flex}
.post .thumb{width:200px;height:130px;box-shadow:0 8px 7px -4px rgba(0,0,0,.5);flex:none}
.post .body{margin-left:20px;width:250px}
.post h4{font-family:"PT Sans",sans-serif;font-weight:400;font-size:13px;line-height:21px;color:#333}
.post .date{margin-top:6px;font-size:10px;color:#555;display:flex;align-items:center;gap:4px}
.post p{margin-top:6px;font-size:10px;line-height:21px;color:#888}

/* Testimonials */
.testimonials{position:absolute;top:1772px;left:0;width:1200px;height:468px;
  background:radial-gradient(ellipse at 50% 40%,#f59a5a 0%,#ec7a35 50%,#d86521 100%)}
.testimonials .section-title{position:absolute;top:66px;width:100%}
.avatar{position:absolute;border-radius:50%;border:3px solid #fff;background:linear-gradient(#d9d4cf,#9d9a97)}
.avatar.main{box-shadow:0 2px 8px rgba(0,0,0,.3)}
.quote-name{position:absolute;top:314px;width:100%;text-align:center;color:#fff;font-family:"Open Sans",sans-serif;font-weight:600;font-size:15px}
.quote{position:absolute;top:344px;left:245px;width:710px;text-align:center;color:#fff;font-size:11px;line-height:26px}

/* Footer */
.footer{position:absolute;top:2240px;left:0;width:1200px;height:200px;background:var(--footer);color:#fff}
.col{position:absolute;top:28px}
.col h3{font-size:19px;font-weight:700}
.col p{margin-top:14px;font-size:11px;line-height:24px;color:#ccc}
.socials{display:flex;gap:11px;margin-top:14px}
.socials span{width:32px;height:32px;border:1px solid #ddd;border-radius:50%}
.signup{margin-top:12px;width:288px;height:42px;background:#fff;border-radius:3px;display:flex;align-items:center;justify-content:space-between;padding:0 6px 0 18px;font-size:11px;color:#888}
.signup .go{width:40px;height:30px;background:var(--green);border-radius:2px;display:flex;align-items:center;justify-content:center}
.contact-row{display:flex;align-items:center;gap:14px;margin-top:16px;font-size:12px;color:#ddd}
.contact-row .ic{width:32px;height:32px;border:1px solid #666;border-radius:50%;display:flex;align-items:center;justify-content:center}
.footer-bar{position:absolute;top:2440px;left:0;width:1200px;height:85px;background:var(--footer-bar);color:#ddd;font-size:11px;text-align:center;padding-top:34px}
</style>
</head>
<body>

<header class="hero" role="img" aria-label="Conference audience photo in blue tones">
  <nav class="nav">
    <div class="brand">Brightpath7go</div>
    <ul class="menu">
      <li class="active">Home</li><li>About Us</li><li>Services</li><li>Events</li><li>News</li><li>Contact Us</li>
      <li class="search"><svg width="13" height="13" viewBox="0 0 13 13"><circle cx="5.5" cy="5.5" r="4" fill="none" stroke="#333" stroke-width="2"/><line x1="8.5" y1="8.5" x2="12" y2="12" stroke="#333" stroke-width="2"/></svg></li>
    </ul>
  </nav>
  <h1 class="hero-title">BUSINESS EVENTS</h1>
  <p class="hero-text">Lorem ipsum dolor sit amet, consectetur adipiscing elit. Etiam vitae venenatis velit. Vestibulum volutpat tortor justo, venenatis scelerisque purus males uada ut. Suspendisse eget tellus non elit rutrum semper id in nulla. Nam tristique hendrerit orci vitae blandit.</p>
  <div class="dots"><span></span><span></span><span class="on"></span><span></span></div>
</header>

<section class="features">
  <div class="feature" style="left:110px">
    <div class="ring"><svg width="46" height="40" viewBox="0 0 46 40" fill="#f37122"><circle cx="23" cy="10" r="7"/><path d="M11 34c0-8 5-13 12-13s12 5 12 13z"/><circle cx="9" cy="14" r="5"/><path d="M0 32c0-6 4-9 9-9 2 0 3 0 4 1-2 2-3 5-3 8z"/><circle cx="37" cy="14" r="5"/><path d="M46 32c0-6-4-9-9-9-2 0-3 0-4 1 2 2 3 5 3 8z"/></svg></div>
    <h3>WHO WE ARE</h3>
    <p>Donec eu nisi eget dui posuere venenatis vel vel elit. Praesent ipsum dolor, ultricies quis arcu ac, tristique hendrerit dolor. Vest ibulum ante ipsum primis in faucibus.</p>
  </div>
  <div class="feature" style="left:450px">
    <div class="ring"><svg width="46" height="42" viewBox="0 0 46 42" fill="#f37122"><circle cx="17" cy="24" r="11"/><g stroke="#f37122" stroke-width="5"><line x1="17" y1="9" x2="17" y2="39"/><line x1="2" y1="24" x2="32" y2="24"/><line x1="6" y1="13" x2="28" y2="35"/><line x1="28" y1="13" x2="6" y2="35"/></g><circle cx="17" cy="24" r="4" fill="#fff"/><circle cx="36" cy="10" r="6"/><circle cx="36" cy="10" r="2.5" fill="#fff"/><circle cx="37" cy="31" r="5"/><circle cx="37" cy="31" r="2" fill="#fff"/></svg></div>
    <h3>WHAT WE DO</h3>
    <p>Morbi nec nunc sit amet sem venenatis condimentum eget tempor sem. Nullam hendrerit vitae purus ac volutpat. Phase llus nisi massa, rhoncus ut malesuada.</p>
  </div>
  <div class="feature" style="left:788px">
    <div class="ring"><svg width="30" height="42" viewBox="0 0 30 42"><path d="M4 12c0-6 5-9 11-9s11 4 11 10c0 8-9 8-9 15" fill="none" stroke="#f37122" stroke-width="6"/><rect x="11" y="33" width="8" height="8" fill="#f37122"/></svg></div>
    <h3>WHY US?</h3>
    <p>Curabitur dui quam, bibendum sed lorem sit amet, molestie dapibus odio. Ut neque magna, consequat id mauris pellent esque, feugiat faucibus erat.</p>
  </div>
</section>

<section class="calendar-section" role="img" aria-label="Concert crowd photo in warm orange tones">
  <h2 class="section-title">EVENT CALENDAR</h2>
  <div class="event-box">
    <div class="month">
      <div class="month-head"><span class="arr">&#9664;</span><span>July 2016</span><span class="arr next">&#9654;</span></div>
      <table class="days">
        <tr><th>SU</th><th>MO</th><th>TU</th><th>WE</th><th>TH</th><th>FR</th><th>SA</th></tr>
        <tr><td class="out">26</td><td class="out">27</td><td class="out">28</td><td class="out">29</td><td class="out">30</td><td>1</td><td class="mark">2</td></tr>
        <tr><td>3</td><td>4</td><td>5</td><td>6</td><td>7</td><td>8</td><td class="sat">9</td></tr>
        <tr><td>10</td><td>11</td><td class="today">12</td><td>13</td><td>14</td><td>15</td><td class="sat">16</td></tr>
        <tr><td>17</td><td>18</td><td>19</td><td>20</td><td>21</td><td class="sel">22</td><td class="sat">23</td></tr>
        <tr><td>24</td><td>25</td><td>26</td><td>27</td><td>28</td><td>29</td><td class="sat">30</td></tr>
        <tr><td>31</td><td class="out">1</td><td class="out">2</td><td class="out">3</td><td class="out">4</td><td class="out">5</td><td class="out">6</td></tr>
      </table>
    </div>
    <div class="agenda">
      <div class="agenda-head">Selected day : 22 July, 2016</div>
      <div class="agenda-item">
        <div class="thumb" role="img" aria-label="Photo of people at a business event" style="background:linear-gradient(#8fa6c4,#3e4f6a)"></div>
        <div class="body">
          <h4>Morbi nec nunc sit amet sem venenatis</h4>
          <p>Sed dui est, auctor at massa quis, scelerisque auctor urna. Vestibulum nec rutrum metus, non vehicula eros. Curabitur interdum.</p>
          <div class="more">&#9656; Read more</div>
        </div>
      </div>
      <div class="agenda-item">
        <div class="thumb" role="img" aria-label="Photo of a seminar room with attendees" style="background:linear-gradient(#dfe6ee,#8aa0b8)"></div>
        <div class="body">
          <h4>Lorem ipsum dolor sit amet</h4>
          <p>Curabitur dui quam, bibendum sed lorem sit amet, molestie dapibus odio. Ut neque magna, consequat id mauris pellentesque, feugiat faucibus erat.</p>
          <div class="more">&#9656; Read more</div>
        </div>
      </div>
    </div>
  </div>
</section>

<section class="latest">
  <h2 class="section-title">LATEST EVENTS</h2>
  <article class="post" style="left:112px">
    <div class="thumb" role="img" aria-label="Event poster with green leaf artwork" style="background:linear-gradient(135deg,#ffffff 40%,#cfe7b0 70%,#5aa83a)"></div>
    <div class="body">
      <h4>Ut wisi enim ad minim veniam, quis nostr ud exerci tation ullamcorper</h4>
      <div class="date"><svg width="10" height="10" viewBox="0 0 10 10"><rect x="0.5" y="1.5" width="9" height="8" fill="none" stroke="#f37122"/><rect x="0.5" y="1.5" width="9" height="2.5" fill="#f37122"/></svg>13 MAY 2016</div>
      <p>Duis autem vel eum iriure dolor in hendrerit in vulputate velit esse molestie consequat, vel illum dolore eu feugiat nulla facilisis..</p>
    </div>
  </article>
  <article class="post" style="left:618px">
    <div class="thumb" role="img" aria-label="Photo of an audience at a talk" style="background:linear-gradient(135deg,#c9d4e2,#6f84a0 60%,#c08a62)"></div>
    <div class="body">
      <h4>Nam ante nibh, cursus nec odio vel, faucibus laoreet nulla. Suspendisse nec tincidu</h4>
      <div class="date"><svg width="10" height="10" viewBox="0 0 10 10"><rect x="0.5" y="1.5" width="9" height="8" fill="none" stroke="#f37122"/><rect x="0.5" y="1.5" width="9" height="2.5" fill="#f37122"/></svg>13 MAY 2016</div>
      <p>Duis autem vel eum iriure dolor in hendrerit in vulputate velit esse molestie consequat, vel illum dolore eu feugiat nulla facilisis..</p>
    </div>
  </article>
</section>

<section class="testimonials" role="img" aria-label="Blurred event crowd photo in orange tones">
  <h2 class="section-title">TESTIMONIALS</h2>
  <div class="avatar" role="img" aria-label="Client portrait" style="left:325px;top:166px;width:82px;height:82px"></div>
  <div class="avatar" role="img" aria-label="Client portrait" style="left:428px;top:166px;width:82px;height:82px"></div>
  <div class="avatar main" role="img" aria-label="Portrait of Clara Denholm" style="left:533px;top:141px;width:130px;height:130px"></div>
  <div class="avatar" role="img" aria-label="Client portrait" style="left:692px;top:166px;width:82px;height:82px"></div>
  <div class="avatar" role="img" aria-label="Client portrait" style="left:796px;top:166px;width:82px;height:82px"></div>
  <div class="quote-name">CLARA DENHOLM</div>
  <p class="quote">Quisque facilisis augue magna, ut ornare augue viverra eu. Nulla facilisi. Pellentesque tempus nec massa sit efficitur. Sed a felis nec libero interdum vestibulum. Fusce sed arcu mauris. Integer condimentum dolor purus, at auctor lacus lobortis vitae.</p>
</section>

<footer class="footer">
  <div class="col" style="left:110px;width:300px">
    <h3>CONNECT WITH US</h3>
    <p>Lorem ipsum dolor sit amet, consectetur adipiscing elit.<br>Suspend e vitae purus blandit.</p>
    <div class="socials"><span></span><span></span><span></span><span></span><span></span></div>
  </div>
  <div class="col" style="left:480px;width:300px">
    <h3>NEWSLETTER SIGNUP</h3>
    <p>Curabitur imperdiet risus id neque aliquet congue mal<br>esuada et nisi.</p>
    <div class="signup">Email Address<span class="go"><svg width="14" height="12" viewBox="0 0 14 12"><path d="M0 6h10M6 1l5 5-5 5" fill="none" stroke="#fff" stroke-width="2.5"/></svg></span></div>
  </div>
  <div class="col" style="left:850px;width:260px">
    <h3>CONTACT US</h3>
    <div class="contact-row" style="margin-top:20px"><span class="ic"><svg width="14" height="14" viewBox="0 0 14 14"><path d="M3 1l2.5 3-1.5 1.5c1 2 2.5 3.5 4.5 4.5L10 8.5l3 2.5-1.5 2C6 13 1 8 1 2.5z" fill="#9bcb3c"/></svg></span>555 010 2040</div>
    <div class="contact-row"><span class="ic"><svg width="14" height="10" viewBox="0 0 14 10"><rect width="14" height="10" rx="1" fill="#9bcb3c"/><path d="M0.5 0.5L7 6l6.5-5.5" fill="none" stroke="#161616" stroke-width="1.3"/></svg></span>info@brightpath7go.example</div>
  </div>
</footer>
<div class="footer-bar">© 2016 Brightpath7go. All Rights Reserved.</div>

</body>
</html>
```